" Nosso corpo jurídico é constituído por profissionais com vasta experiência na advocacia. A reunião desses profissionais e o amadurecimento de um ideal comum, resultaram na criação de um grupo comprometido com a prestação de serviços jurídicos. Estamos aptos a atender, com eficiência, agilidade e qualidade, atuando em equipe ou individualmente para solução do seu problema, por meio de métodos eficientes e dinâmicos. "

```html
<!DOCTYPE html>
<html lang="pt-BR">
<head>
<meta charset="utf-8">
<title>Moreira Tavares &amp; Lins — Papel Timbrado</title>
<link href="https://fonts.googleapis.com/css2?family=Lato:wght@400;700&display=swap" rel="stylesheet">
<style>
  :root {
    --backdrop: #e9e9e7;
    --paper: #ffffff;
    --ink: #2f2b29;
    --ink-soft: #6f6a66;
    --bronze: #b28b5f;
    --band-dark: #2b2523;
    --watermark: #f2f2f1;
  }
  * { margin: 0; padding: 0; box-sizing: border-box; }
  html, body {
    width: 1200px; height: 1200px; overflow: hidden;
    background: var(--backdrop);
    font-family: "Lato", Arial, sans-serif;
    color: var(--ink);
  }
  .letterhead {
    position: absolute; left: 211px; top: 50px;
    width: 778px; height: 1100px;
    background: var(--paper);
    box-shadow: 0 6px 24px rgba(0,0,0,.12);
    overflow: hidden;
  }
  .watermark {
    position: absolute; left: 250px; top: 330px;
    width: 300px; height: 300px;
    border: 40px solid var(--watermark);
  }
  .brand {
    position: absolute; right: 64px; top: 60px;
    display: flex; align-items: center; gap: 12px;
  }
  .brand-square { width: 40px; height: 40px; background: var(--bronze); }
  .brand-name {
    font-size: 15px; font-weight: 700; letter-spacing: 1.5px;
    text-transform: uppercase; line-height: 1.25; color: var(--bronze);
  }
  .recipient {
    position: absolute; left: 70px; top: 150px;
    font-size: 13px; line-height: 1.45; font-weight: 700;
  }
  .recipient .label { font-weight: 400; color: var(--ink-soft); }
  .meta {
    position: absolute; right: 64px; top: 290px;
    text-align: right; font-size: 11px; line-height: 1.6; color: var(--ink-soft);
  }
  .body-copy {
    position: absolute; left: 70px; top: 350px; width: 638px;
    font-size: 12px; line-height: 1.75; color: var(--ink-soft);
  }
  .body-copy p { margin-bottom: 16px; text-align: justify; }
  .sign-off {
    position: absolute; left: 70px; top: 760px;
    font-size: 12px; color: var(--ink-soft);
  }
  .signature {
    width: 150px; height: 46px; margin: 12px 0 6px;
    background: linear-gradient(90deg, #d9d6d3, #f4f3f2);
    border-radius: 4px;
  }
  .signer { font-weight: 700; color: var(--ink); }
  .contact-bar {
    position: absolute; left: 70px; right: 64px; top: 985px;
    display: flex; justify-content: space-between;
    font-size: 10px; color: var(--ink-soft);
  }
  .contact-item { display: flex; align-items: center; gap: 6px; }
  .contact-item svg { width: 12px; height: 12px; fill: none; stroke: var(--bronze); stroke-width: 1.6; }
  .footer-band {
    position: absolute; left: 0; right: 0; bottom: 0; height: 42px; display: flex;
  }
  .footer-band .dark { flex: 1; background: var(--band-dark); }
  .footer-band .bronze { width: 190px; background: var(--bronze); }
</style>
</head>
<body>
<main class="letterhead">
  <div class="watermark" aria-hidden="true"></div>

  <header class="brand">
    <div class="brand-square"></div>
    <div class="brand-name">Moreira Tavares<br>&amp; Lins<br>Advogados</div>
  </header>

  <section class="recipient">
    <div class="label">Para</div>
    Sr. Renato Alves<br>
    Diretor Executivo<br>
    Grupo Atlântico<br>
    Av. Central, 500<br>
    Recife, PE 50030
  </section>

  <section class="meta">
    Ref.: 021/2024<br>
    Recife, 14 de março de 2024
  </section>

  <section class="body-copy">
    <p>Prezado senhor, apresentamos nosso escritório e a equipe que atua em direito empresarial, civil e tributário, com atendimento próximo e soluções claras para cada caso.</p>
    <p>Nossa experiência reúne profissionais dedicados que trabalham em equipe ou de forma individual, sempre com eficiência, agilidade e qualidade na condução dos processos e contratos.</p>
    <p>Ficamos à disposição para uma reunião em data oportuna e agradecemos a atenção dispensada a esta carta.</p>
  </section>

  <section class="sign-off">
    Atenciosamente,
    <div class="signature" role="img" aria-label="Assinatura manuscrita"></div>
    <div class="signer">Helena Moreira</div>
    Sócia Fundadora
  </section>

  <footer class="contact-bar">
    <span class="contact-item">
      <svg viewBox="0 0 12 12"><circle cx="6" cy="6" r="5"/><path d="M1 6h10M6 1c2 2 2 8 0 10M6 1c-2 2-2 8 0 10"/></svg>
      www.moreiratavares.adv.br
    </span>
    <span class="contact-item">
      <svg viewBox="0 0 12 12"><rect x="1" y="2.5" width="10" height="7"/><path d="M1 2.5l5 4 5-4"/></svg>
      contato@moreiratavares.adv.br
    </span>
    <span class="contact-item">
      <svg viewBox="0 0 12 12"><path d="M2 1.5h2.5l1 2.5-1.5 1a6 6 0 0 0 3 3l1-1.5 2.5 1V10a1 1 0 0 1-1 1A9 9 0 0 1 1 2.5a1 1 0 0 1 1-1z"/></svg>
      +55 81 3000-0000
    </span>
    <span class="contact-item">
      <svg viewBox="0 0 12 12"><path d="M6 11S2 7 2 4.5a4 4 0 0 1 8 0C10 7 6 11 6 11z"/><circle cx="6" cy="4.5" r="1.4"/></svg>
      Rua das Flores, 100 - Recife
    </span>
  </footer>

  <div class="footer-band"><div class="dark"></div><div class="bronze"></div></div>
</main>
</body>
</html>
```